Kestrelwood Pathways Agency business cards

Australian company about to start offering its services. We recruit international students to come to study English, vocational education and postgraduate courses in Australia. We help them find the institution and select the right city they want to come to Australia. We are a young, online oriented and supportive agency. Our clients are between 18 and 35 years old, mainly University students, young professionals or people with work experience. We provide much more information that any other agency offer. We administrate a Facebook group with more than 11.000 members that daily ask questions about general information when coming to Australia, while they are here and even after they leave the country

Target Market(s)

International students from South America, Central America and Europe

Industry/Entity Type

Student

Contact Information for Business Card

Tomas Brevik
Managing Director
tomas@velmorin.com.au
www.velmorin.com.au
+61 491058263
Melbourne, Australia

Font styles to use
Serif
Sans Serif

Colors

Designer to choose colors to be used in the design.

Requirements
Must have
• Horizontal design
• Standard business card size and shape. If font uses green or yellow colours, they will have to match the ones from the logo
Nice to have
• UPDATE: Use the contents of the green image to design one of the card sides. Use our logo in the background of that side as watermark.
• Passport image, or immigration stamps. A picture of the Yarra River (from Melbourne) would be cool as well.
Should not have
• Non-standard business card size and shape
• Not black as the background colour of any sides as we are not a VIP agency or a hight class service. We are orientes to young people and they like colours, pictures, something attractive.
• Vertical design
• NO YELLOW or BLACK AS THE BACKGROUND COLOUR OF ANY SIDE OF THE BIZ CARD

```html
<!DOCTYPE html>
<html lang="en">
<head>
<meta charset="utf-8">
<title>Kestrelwood Pathways Agency business cards</title>
<link rel="stylesheet" href="https://fonts.googleapis.com/css2?family=Ubuntu:ital,wght@0,400;0,500;1,400&display=swap">
<style>
  :root {
    --brand-green: #17704a;
    --brand-yellow: #eec21f;
    --brand-navy: #1c2466;
    --panel-grey: #b4b5b8;
    --card-white: #f4f4f4;
    --backdrop: #e6e8eb;
  }
  * { margin: 0; padding: 0; box-sizing: border-box; }
  html, body {
    width: 1200px;
    height: 900px;
    overflow: hidden;
    background: var(--backdrop);
    font-family: "Ubuntu", sans-serif;
  }
  .card-set {
    width: 1200px;
    height: 900px;
    display: flex;
    flex-direction: column;
    align-items: center;
    justify-content: center;
    gap: 56px;
  }
  .business-card {
    width: 640px;
    height: 366px;
    display: block;
    box-shadow: 0 6px 18px rgba(0, 0, 0, 0.18);
  }
  .fill-white { fill: var(--card-white); }
  .fill-green { fill: var(--brand-green); }
  .fill-yellow { fill: var(--brand-yellow); }
  .fill-navy { fill: var(--brand-navy); }
  .hex-panel { fill: var(--panel-grey); stroke: var(--brand-green); stroke-width: 8; stroke-linejoin: miter; }
  .accent-stroke { stroke: var(--brand-yellow); fill: none; }
  .card-text { font-family: "Ubuntu", sans-serif; }
  .holder-name { font-size: 38px; font-weight: 500; }
  .holder-role { font-size: 14px; letter-spacing: 5px; fill: var(--brand-green); }
  .contact-line { font-size: 16px; fill: var(--brand-green); }
  .brand-name { font-size: 44px; font-weight: 500; fill: var(--brand-green); }
  .tagline { font-size: 20px; font-style: italic; fill: var(--brand-yellow); }
  .web-address { font-size: 17px; font-style: italic; fill: var(--brand-green); }
  .icon { fill: var(--brand-yellow); }
</style>
</head>
<body>
<main class="card-set">

  <!-- Brand side -->
  <svg class="business-card brand-side" viewBox="0 0 700 400" aria-label="Card brand side">
    <rect class="fill-white" x="0" y="0" width="700" height="400"/>
    <rect class="fill-yellow" x="0" y="0" width="700" height="34"/>
    <rect class="fill-green" x="0" y="296" width="700" height="48"/>
    <rect class="fill-yellow" x="0" y="344" width="700" height="56"/>
    <polygon class="fill-navy" points="72,254 420,254 392,318 44,318"/>
    <text class="card-text tagline" x="232" y="293" text-anchor="middle">Hacemos más por ti!</text>

    <circle class="fill-yellow" cx="96" cy="118" r="13"/>
    <text class="card-text brand-name" x="120" y="133">Velmorin</text>

    <text class="card-text web-address" x="440" y="206">www.velmorin.com.au</text>
    <line class="accent-stroke" x1="604" y1="201" x2="700" y2="201" stroke-width="2"/>
  </svg>

  <!-- Contact side -->
  <svg class="business-card contact-side" viewBox="0 0 700 400" aria-label="Card contact side">
    <rect class="fill-white" x="0" y="0" width="700" height="400"/>

    <rect class="fill-yellow" x="40" y="36" width="5" height="54"/>
    <text class="card-text holder-name" x="58" y="74">
      <tspan class="fill-green">Tomas </tspan><tspan class="fill-yellow">Brevik</tspan>
    </text>
    <text class="card-text holder-role" x="60" y="100">Managing Director</text>

    <g class="contact-list">
      <path class="icon" d="M42 152 L54 146 L48 158 L47 153 Z"/>
      <text class="card-text contact-line" x="64" y="158">Melbourne, Australia</text>

      <path class="icon" d="M42 177 q0 10 10 12 l2 -3 l-3 -3 l-2 1 q-3 -2 -4 -5 l1 -2 l-3 -3 z"/>
      <text class="card-text contact-line" x="64" y="188">+61 491058263</text>

      <circle class="icon" cx="48" cy="212" r="6.5"/>
      <text class="card-text contact-line" x="64" y="218">www.velmorin.com.au</text>

      <rect class="icon" x="41" y="237" width="14" height="10"/>
      <path d="M41 237 L48 243 L55 237" stroke="var(--card-white)" stroke-width="1.4" fill="none"/>
      <text class="card-text contact-line" x="64" y="248">tomas@velmorin.com.au</text>
    </g>

    <rect class="fill-yellow" x="520" y="110" width="180" height="10"/>
    <line class="accent-stroke" x1="246" y1="296" x2="290" y2="400" stroke-width="10"/>
    <polygon class="hex-panel" points="335,404 270,256 382,132 704,132 704,404"/>

    <circle class="fill-yellow" cx="418" cy="262" r="13"/>
    <text class="card-text brand-name" x="442" y="277">Velmorin</text>
  </svg>

</main>
</body>
</html>
```